Town of Pellbrook Commercial Development

Create introduction point with 3 subheading categories. The bullets under the 3 categories should be where to use the infographics. Keep the Town of Pellbrook logo in the piece. The layout can be vertical or horizontal. Would like to stay on one page.

Target Market(s)

Commercial real estate developers and corporations

Industry/Entity Type

Real estate

Font styles to use
Serif

Requirements
Must have
• Business to business looking
Should not have
• Not comical

```html
<!DOCTYPE html>
<html lang="en">
<head>
<meta charset="utf-8">
<title>Town of Pellbrook – Commercial Development</title>
<link rel="stylesheet" href="https://fonts.googleapis.com/css2?family=Merriweather:wght@400;700;900&family=Open+Sans:wght@400;600;700&display=swap">
<style>
:root{
  --maroon:#7c2216;
  --rust:#9a3322;
  --teal:#264a53;
  --ink:#3b4f55;
  --paper:#f7f1ee;
  --card:#f6ece8;
  --tint:#e8d3cc;
  --line:#264a53;
  --stage:#2c2c2c;
  --serif:"Merriweather",Georgia,serif;
  --sans:"Open Sans",Arial,sans-serif;
}
*{box-sizing:border-box;margin:0;padding:0}
html,body{width:1200px;height:1177px;overflow:hidden;background:var(--stage)}
.sheet{position:absolute;left:202px;top:74px;width:796px;height:1030px;background:linear-gradient(#fff 0,var(--paper) 200px,var(--paper) 100%);font-family:var(--sans);color:var(--ink);overflow:hidden}
.abs{position:absolute}
.seal{left:33px;top:26px;width:176px;height:176px;border-radius:50%;background:#fff;border:3px solid var(--rust);z-index:3;display:flex;flex-direction:column;align-items:center;justify-content:center;gap:8px}
.seal-mark{width:22px;height:22px;background:var(--maroon)}
.seal-name{font-family:var(--serif);font-weight:700;font-size:21px;color:var(--maroon);text-align:center;line-height:1.1}
.headline{left:208px;top:43px;width:570px;height:46px;background:var(--maroon);border-radius:0 18px 0 0;color:#fff;font-family:var(--serif);font-weight:400;font-size:23px;display:flex;align-items:center;padding-left:30px;z-index:2}
.headline b{font-weight:900}
.intro{left:150px;top:89px;width:628px;height:86px;background:var(--teal);color:#fff;font-size:15.5px;line-height:1.25;padding:10px 20px 0 88px}
.intro strong{font-weight:700}
.section-title{left:0;width:796px;top:212px;text-align:center;font-family:var(--serif);font-weight:700;font-size:30px;color:var(--maroon);letter-spacing:.5px}
.section-title span{color:var(--teal)}
.location{left:22px;top:253px;width:756px;height:318px;background:var(--teal)}
.card{position:absolute;background:var(--card);border:2px solid #d49a8c;border-radius:8px;text-align:center;font-size:12.5px;line-height:1.2;color:var(--ink);padding:8px;display:flex;flex-direction:column;align-items:center;justify-content:center}
.card b{color:var(--maroon)}
.card .teal{color:var(--teal)}
.icon{display:block;background:var(--tint);border-radius:6px;margin:0 auto}
.map-ring{left:290px;top:8px;width:206px;height:206px;border-radius:50%;background:#fff;padding:6px}
.map{width:100%;height:100%;border-radius:50%;background:linear-gradient(135deg,#bcd3de,#dfe6d9 45%,#e7e2dc)}
.bullets{left:224px;top:236px;width:300px;color:#fff;font-size:12.5px;line-height:1.3;list-style:none}
.bullets li::before{content:"• "}
.bullets li{padding-left:10px;text-indent:-10px}
.tab{top:594px;height:42px;background:var(--maroon);color:#fff;font-family:var(--serif);font-weight:700;font-size:24px;display:flex;align-items:center}
.tab-community{left:0;width:252px;border-radius:0 12px 12px 0;padding-left:20px}
.tab-business{left:564px;width:232px;border-radius:12px 0 0 12px;padding-left:22px}
.note{font-size:12px;line-height:1.2;text-align:center;color:var(--ink)}
.note b{color:var(--teal)}
.note .hi{color:var(--maroon);font-weight:700}
.rule-v{width:2px;background:var(--line)}
.rule-h{height:2px;background:var(--line)}
.employers{left:430px;top:682px;width:156px;text-align:center;font-size:12px;line-height:1.2}
.employers b{color:var(--teal)}
.brands{display:grid;grid-template-columns:1fr 1fr;gap:6px;margin-top:14px}
.brand{background:#fff;height:30px;border-radius:3px;display:flex;align-items:center;justify-content:center;font-size:8.5px;font-weight:700;color:var(--teal);box-shadow:0 1px 2px rgba(0,0,0,.15);line-height:1}
.footer{left:0;top:991px;width:796px;height:39px;background:var(--teal);color:#dfe7e9;font-size:11px;font-style:italic;padding:13px 0 0 36px}
.url{left:528px;top:969px;width:272px;height:42px;background:var(--maroon);border:3px solid #fff;border-radius:22px 0 0 22px;color:#fff;font-family:var(--serif);font-weight:700;font-size:17px;display:flex;align-items:center;justify-content:center}
</style>
</head>
<body>
<main class="sheet">
  <div class="abs seal">
    <span class="seal-mark"></span>
    <span class="seal-name">Town of<br>Pellbrook</span>
  </div>
  <h1 class="abs headline">Locating your business in&nbsp;<b>PELLBROOK</b></h1>
  <p class="abs intro"><strong>could be the smartest move your company ever makes.</strong><br>Our location, employment base, smart growth and college town charm make it a stand-out from other communities.</p>

  <h2 class="abs section-title"><span>1.</span> LOCATION</h2>
  <section class="abs location">
    <div class="card" style="left:16px;top:10px;width:199px;height:137px">
      <div style="display:flex;justify-content:center;gap:10px;align-items:center;height:56px">
        <svg width="56" height="56" viewBox="0 0 62 62" aria-label="40 percent pie chart"><circle cx="31" cy="31" r="30" fill="var(--teal)"/><path d="M31 31 L31 1 A30 30 0 0 1 31 61 Z" fill="var(--maroon)"/><text x="37" y="35" font-family="Open Sans,Arial,sans-serif" font-size="11" font-weight="700" fill="#fff">40%</text></svg>
        <span class="icon" role="img" aria-label="Crowd of people icon" style="width:40px;height:36px;margin:0"></span>
      </div>
      <p style="margin-top:6px">Within a day's drive of <b>40% of the U.S. population</b>, making business close to suppliers &amp; customers alike</p>
    </div>
    <div class="card" style="left:16px;top:168px;width:199px;height:138px">
      <span class="icon" role="img" aria-label="Control tower and departing airplane icon" style="width:100px;height:62px"></span>
      <p style="margin-top:8px"><b class="teal">30 minutes</b> from Ashford International Airport</p>
    </div>
    <div class="abs map-ring"><div class="map" role="img" aria-label="Area map showing Pellbrook and the lake north of Ashford"></div></div>
    <ul class="abs bullets">
      <li>Located in the Ashford MSA</li>
      <li>Pellbrook is just 20 miles north of<br>Ashford, NC in Harlow County</li>
      <li>Conveniently located off 1-77 &amp; State Highway 73</li>
    </ul>
    <div class="card" style="left:542px;top:10px;width:199px;height:139px">
      <span class="icon" style="width:30px;height:30px;background:var(--maroon)"></span>
      <p style="font-family:var(--serif);font-weight:900;font-size:20px;color:var(--teal);margin-top:10px">PELLBROOK</p>
      <p style="margin-top:6px">Home of <b class="teal">Pellbrook College</b></p>
    </div>
    <div class="card" style="left:542px;top:170px;width:199px;height:136px;flex-direction:row;gap:8px">
      <div style="width:82px"><span class="icon" role="img" aria-label="Beach umbrella icon" style="width:60px;height:50px"></span><p style="margin-top:8px"><b class="teal">3 hours</b><br>to beautiful beaches</p></div>
      <div style="width:82px"><span class="icon" role="img" aria-label="Mountains icon" style="width:60px;height:50px"></span><p style="margin-top:8px"><b class="teal">2 hours</b><br>to scenic mountains</p></div>
    </div>
  </section>

  <h2 class="abs tab tab-community">2. COMMUNITY</h2>
  <h2 class="abs tab tab-business">3. BUSINESS</h2>

  <div class="abs" style="left:16px;top:660px;width:170px;display:flex;justify-content:space-between">
    <div class="note" style="width:84px"><span class="icon" role="img" aria-label="Growing population icon" style="width:76px;height:46px"></span><p style="margin-top:4px;font-size:11px">population<br>of <span class="hi">15,132</span></p></div>
    <div class="note" style="width:84px"><span class="icon" role="img" aria-label="Hand holding money bag icon" style="width:46px;height:46px"></span><p style="margin-top:4px;font-size:11px">median income<br>of <span class="hi">$131,144</span></p></div>
  </div>
  <p class="abs note" style="left:18px;top:752px;width:172px">one of the <b>fastest growing</b> affluent populations in North Carolina</p>
  <div class="abs rule-v" style="left:196px;top:674px;height:126px"></div>
  <svg class="abs" style="left:246px;top:662px" width="66" height="66" viewBox="0 0 70 70" aria-label="74 percent pie chart"><circle cx="35" cy="35" r="34" fill="var(--teal)"/><path d="M35 35 L35 1 A34 34 0 1 1 1.3 30.2 Z" fill="var(--maroon)"/><text x="16" y="50" font-family="Open Sans,Arial,sans-serif" font-size="11" font-weight="700" fill="#fff">&gt;74%</text></svg>
  <span class="abs icon" role="img" aria-label="Graduation cap and diploma icon" style="left:322px;top:670px;width:62px;height:46px"></span>
  <p class="abs note" style="left:208px;top:738px;width:196px;text-align:left">More than 74% of Pellbrook's residents over the age of 25 hold a <b>bachelor's degree / higher</b></p>
  <div class="abs rule-h" style="left:22px;top:812px;width:344px"></div>
  <span class="abs icon" role="img" aria-label="Number one ranking with heart and people icon" style="left:42px;top:832px;width:98px;height:58px"></span>
  <p class="abs note" style="left:22px;top:898px;width:166px">In national citizen surveys, Pellbrook ranks #1 in <b>"sense of community"</b></p>
  <div class="abs rule-v" style="left:196px;top:830px;height:140px"></div>
  <span class="abs icon" role="img" aria-label="Park, celebration and low crime icons" style="left:208px;top:826px;width:176px;height:58px"></span>
  <p class="abs note" style="left:208px;top:890px;width:206px;text-align:left">Pellbrook's lake amenities, parks, greenways, first-rate schools, low crime rate &amp; proximity to Pellbrook College make it a <b>great place to live and work.</b></p>

  <div class="abs employers">
    <p>Pellbrook's <b>major employers</b> include</p>
    <div class="brands">
      <span class="brand">NORTHVALE TECH</span><span class="brand">KEYSTONE SUPPLY</span>
      <span class="brand">BRIGHTLINE TOOLS</span><span class="brand">PELLBROOK</span>
    </div>
  </div>
  <div class="abs rule-v" style="left:592px;top:672px;height:126px"></div>
  <span class="abs icon" role="img" aria-label="Farmers market stall and restaurant icons" style="left:624px;top:664px;width:130px;height:56px"></span>
  <p class="abs note" style="left:604px;top:728px;width:184px;text-align:left">Pellbrook has a thriving <b>Farmer's Market</b> &amp; is home to <b>over 30 restaurants</b> including Harvest Table Award nominees.</p>
  <div class="abs rule-h" style="left:438px;top:812px;width:340px"></div>
  <span class="abs icon" role="img" aria-label="Funding, storefront and networking icons" style="left:510px;top:826px;width:216px;height:60px"></span>
  <p class="abs note" style="left:460px;top:894px;width:326px;text-align:left">Pellbrook promotes a culture of <b>supporting local independent businesses</b> through our active business retention program, various <b>funding</b> programs, and small business <b>networking</b> opportunities.</p>

  <footer class="abs footer">Icons by Linecraft from Iconhub.com</footer>
  <a class="abs url">www.townofpellbrook.org</a>
</main>
</body>
</html>
```